Professional Photography Business cards

I need business cards that include my logo which I have uploaded. I run a photography business. I am open to ideas but I would like one side to have my logo and the other side to have my contact info. I don't have a website made but I do own a website domain. I have uploaded 2 different logo color schemes. My business colors are Blue, black , and white.

Business Name
Business Phone Number
Business Email
Business Website address
Instagram

Industry/Entity Type

Professional Photography

Contact Information for Business Card

Phone Number: 555-314-8027 email: info@tkellan-studios.example Instagram: @t.kellanstudios website doman- www.tkellan-studios.example

Requirements
Must have
• I like the idea of a business card with a full black background front and back of card. My colors must include royal blue, black, and white

```html
<!DOCTYPE html>
<html lang="en">
<head>
<meta charset="utf-8">
<title>T. Kellan Photography – Business Cards</title>
<link rel="stylesheet" href="https://fonts.googleapis.com/css2?family=Roboto:wght@300;400;700&display=swap">
<style>
  :root {
    --royal-blue: #3f5ee8;
    --card-black: #0d0d10;
    --white: #ffffff;
    --ink: #d9dae0;
    --rule: #3f5ee8;
    --backdrop: #e8e9ec;
    --shadow: rgba(10, 12, 30, 0.28);
  }
  * { box-sizing: border-box; margin: 0; padding: 0; }
  html, body {
    width: 1200px;
    height: 800px;
    overflow: hidden;
    background: var(--backdrop);
    font-family: "Roboto", Arial, sans-serif;
  }
  .stage {
    position: relative;
    width: 1200px;
    height: 800px;
  }
  .card {
    position: absolute;
    top: 257px;
    width: 500px;
    height: 286px;
    background: var(--card-black);
    box-shadow: 0 10px 26px var(--shadow);
  }
  .card--front { left: 70px; border-bottom: 6px solid var(--royal-blue); }
  .card--back  { left: 630px; border-bottom: 6px solid var(--royal-blue); }

  /* brand mark: plain circle + name */
  .brand {
    display: flex;
    align-items: center;
    gap: 12px;
    font-weight: 400;
    letter-spacing: 0.14em;
    text-transform: uppercase;
    white-space: nowrap;
    color: var(--white);
  }
  .brand__dot {
    border-radius: 50%;
    flex: none;
    border: 2px solid var(--royal-blue);
  }
  .card--front .brand {
    position: absolute;
    left: 50%;
    top: 50%;
    transform: translate(-50%, -50%);
    font-size: 22px;
  }
  .card--front .brand__dot { width: 34px; height: 34px; }
  .card--back .brand {
    position: absolute;
    left: 40px;
    top: 72px;
    font-size: 14px;
  }
  .card--back .brand__dot { width: 24px; height: 24px; }

  .holder {
    position: absolute;
    right: 34px;
    top: 30px;
    text-align: right;
  }
  .holder__name {
    color: var(--royal-blue);
    font-weight: 700;
    font-size: 17px;
    letter-spacing: 0.02em;
  }
  .holder__title {
    color: var(--ink);
    font-size: 13px;
    margin-top: 2px;
  }
  .holder__address {
    color: var(--ink);
    font-size: 13px;
    line-height: 1.4;
    margin-top: 20px;
  }

  .divider {
    position: absolute;
    left: 40px;
    right: 34px;
    top: 138px;
    height: 1px;
    background: var(--rule);
  }

  .contacts {
    position: absolute;
    left: 40px;
    top: 158px;
    list-style: none;
  }
  .contacts__item {
    display: flex;
    align-items: center;
    gap: 8px;
    color: var(--white);
    font-size: 15px;
    line-height: 1;
    margin-bottom: 9px;
  }
  .contacts__icon {
    width: 13px;
    height: 13px;
    flex: none;
    fill: var(--royal-blue);
  }
</style>
</head>
<body>
<main class="stage">

  <section class="card card--front" aria-label="Card front">
    <div class="brand">
      <span class="brand__dot"></span>
      <span class="brand__name">T. Kellan Photography</span>
    </div>
  </section>

  <section class="card card--back" aria-label="Card back">
    <div class="brand">
      <span class="brand__dot"></span>
      <span class="brand__name">T. Kellan Photography</span>
    </div>

    <div class="holder">
      <p class="holder__name">TESSA KELLAN</p>
      <p class="holder__title">Lead Photographer</p>
      <p class="holder__address">2215 Maple Crest Way<br>Fairhaven, Oh 45099</p>
    </div>

    <div class="divider"></div>

    <ul class="contacts">
      <li class="contacts__item">
        <svg class="contacts__icon" viewBox="0 0 16 16" aria-hidden="true">
          <path d="M3.2 1.2l2.4-.2 1.3 3.2-1.6 1.1c.8 1.8 2.1 3.2 3.9 4l1.1-1.6 3.2 1.3-.2 2.4c-.1.9-.9 1.6-1.8 1.5C6.2 12.6 2.4 8.8 1.8 3c-.1-.9.5-1.7 1.4-1.8z"/>
        </svg>
        <span>555.314.8027</span>
      </li>
      <li class="contacts__item">
        <svg class="contacts__icon" viewBox="0 0 16 16" aria-hidden="true">
          <path d="M1 3h14v10H1z M2.2 4.2v.4L8 8.8l5.8-4.2v-.4z" fill-rule="evenodd"/>
        </svg>
        <span>info@tkellan-studios.example</span>
      </li>
      <li class="contacts__item">
        <svg class="contacts__icon" viewBox="0 0 16 16" aria-hidden="true">
          <circle cx="8" cy="8" r="7"/>
          <path d="M1.5 8h13M8 1.2c2.2 2 2.2 11.6 0 13.6M8 1.2c-2.2 2-2.2 11.6 0 13.6" stroke="#0d0d10" stroke-width="1" fill="none"/>
        </svg>
        <span>www.tkellan-studios.example</span>
      </li>
      <li class="contacts__item">
        <svg class="contacts__icon" viewBox="0 0 16 16" aria-hidden="true">
          <circle cx="8" cy="8" r="6"/>
        </svg>
        <span>@t.kellanstudios</span>
      </li>
    </ul>
  </section>

</main>
</body>
</html>
```